Photo/Video Company needs a business card design

We need a business card design for a photo/video production company called 'Brightwave Studios'. We primarily do wedding photography and videography, however we also do commercial, corporate, and promo work.

We would like a clean, white design that primarily markets us as a wedding photo/video company, but still sleek enough that we attract corporate and commercial clients.

Industry/Entity Type

Wedding

Requirements
Must have
• We wish the front of the business card to simply have the logo, and the back will have the contact information:

Brightwave Studios
Wedding, Event, Corporate, Commercial, Promo
647-518-2736
info@brightwavestudios.example
www.brightwavestudios.example

We are hoping for a version of the card that has only the companies name on it, as well as several variations that have different employees names printed.

The employee names and titles are:

Teo Lindqvar - Photo/Video
Dilan Lindqvar - Photo/Video
Pieter Kalbrook -Video
Odile Brunvik -Photo/Video

The design should use similar fonts in the writing as the fonts used in the logo design. The AI file will be provided.
Nice to have
• We also might like to see the front of the card have the main logo, as well as 'Wedding, Event, Corporate, Commercial, Promo' written in the bottom corner.
Should not have
• No old style fonts should be used. Also no other graphic images should be created, but we are open to the possibility of having shapes and borders.

```html
<!DOCTYPE html>
<html lang="en">
<head>
<meta charset="utf-8">
<title>Brightwave Studios – Business Card</title>
<link rel="stylesheet" href="https://fonts.googleapis.com/css2?family=Questrial&display=swap">
<style>
  :root {
    --brand-red: #e0241b;
    --ink: #2b2b2b;
    --ink-soft: #555555;
    --paper: #ffffff;
    --paper-edge: #e9ebed;
    --divider: #f3c9c6;
  }
  * { margin: 0; padding: 0; box-sizing: border-box; }
  html, body {
    width: 1051px;
    height: 1200px;
    overflow: hidden;
    background: var(--paper);
    font-family: "Questrial", "Century Gothic", sans-serif;
    color: var(--ink);
  }
  .card {
    position: absolute;
    left: 0;
    width: 1051px;
    background: radial-gradient(ellipse 65% 60% at 50% 45%, var(--paper) 45%, var(--paper-edge) 100%);
  }
  .card--front { top: 0; height: 605px; }
  .card--back  { top: 605px; height: 595px; }

  .brand {
    position: absolute;
    display: flex;
    align-items: center;
    gap: 22px;
    color: var(--brand-red);
    text-transform: uppercase;
    white-space: nowrap;
    letter-spacing: 1px;
  }
  .brand__mark {
    width: 30px;
    height: 30px;
    background: var(--brand-red);
    flex: none;
  }
  .card--front .brand {
    left: 0; right: 0;
    top: 295px;
    justify-content: center;
    font-size: 60px;
  }
  .services-line {
    position: absolute;
    left: 0; right: 0;
    top: 497px;
    text-align: center;
    font-size: 21px;
    color: var(--ink);
    letter-spacing: 0.5px;
  }
  .services-line .sep { color: var(--brand-red); margin: 0 8px; }

  .card--back .brand {
    left: 120px;
    top: 148px;
    font-size: 56px;
  }
  .contact {
    position: absolute;
    left: 288px;
    top: 300px;
  }
  .contact__name {
    font-size: 38px;
    color: var(--brand-red);
    line-height: 1.05;
  }
  .contact__services {
    font-size: 27px;
    color: var(--ink);
    margin-top: 4px;
  }
  .contact__list {
    list-style: none;
    margin-top: 16px;
  }
  .contact__item {
    display: flex;
    align-items: baseline;
    height: 31px;
  }
  .contact__label {
    width: 200px;
    text-align: right;
    font-size: 14px;
    color: var(--ink-soft);
  }
  .contact__bullet { font-size: 20px; margin: 0 7px 0 6px; color: var(--ink); }
  .contact__value { font-size: 26px; color: var(--ink); }
</style>
</head>
<body>
  <section class="card card--front">
    <div class="brand"><span class="brand__mark"></span><span class="brand__name">Brightwave Studios</span></div>
    <p class="services-line">wedding<span class="sep">|</span>event<span class="sep">|</span>corporate<span class="sep">|</span>commercial<span class="sep">|</span>prom</p>
  </section>

  <section class="card card--back">
    <div class="brand"><span class="brand__mark"></span><span class="brand__name">Brightwave Studios</span></div>
    <div class="contact">
      <h1 class="contact__name">Brightwave Studios</h1>
      <p class="contact__services">Wedding, Event, Corporate, Commercial, Promo</p>
      <ul class="contact__list">
        <li class="contact__item"><span class="contact__label">phone</span><span class="contact__bullet">•</span><span class="contact__value">647-518-2736</span></li>
        <li class="contact__item"><span class="contact__label">email</span><span class="contact__bullet">•</span><span class="contact__value">info@brightwavestudios.example</span></li>
        <li class="contact__item"><span class="contact__label">website</span><span class="contact__bullet">•</span><span class="contact__value">www.brightwavestudios.example</span></li>
      </ul>
    </div>
  </section>
</body>
</html>
```